Book Cover: A Quiet Cartographer

DO NOT JUST COPY THE BOOK COVER I HAVE ADDED FOR REFERENCE. I NEED SOMETHING FRESH NOT JUST A COPY AND PASTE!
If you cannot improve on the design with something creative then don't submit a design.

Project Title:
Book Cover Design for A Quiet Cartographer

Must be better than the mock design I have uploaded in project files.

Project Description:
I’m looking for a striking and emotionally evocative book cover for my upcoming title A Quiet Cartographer. This is a deeply personal and powerful memoir about the masks we wear, emotional survival, control, and the journey toward radical self-awareness and healing. The cover should visually represent the contrast between the performative self and the authentic self.

Visual Concept:
Please take visual inspiration and design continuity from my previous book Run FAR Now! — I will upload that cover for reference. This new design should feel like a continuation of the same author journey, but bolder and more psychologically intense.

You’ll be provided with two photos of me:

One where I appear more unkept, raw, and emotionally heavy.

One where I appear clean, centered, and lighter.

These can either be:

Split down the middle to create a “mirror” or duality effect (symbolizing the split self),

Or placed side by side as a subtle before/after or internal/external representation.

You may also consider overlaying or fading one into the other if done tastefully.

The mood should hint at internal conflict, self-reckoning, and healing—but without looking too “self-help cliché.” Think masculine, introspective, modern, and editorial. Avoid overly bright or busy visuals. A minimal or clean design with strong type hierarchy is preferred.

Key Themes to Represent Visually (even abstractly):

Narcissism as a survival mechanism

The emotional cost of performance

The tension between image and authenticity

The healing journey from ego to empathy

Design References:

Run FAR Now! (uploaded) — continuity of brand and typography encouraged

Memoir-style covers like Lanterns Along the Winter Harbour, Saltwater, or A Kettle Hums at Dusk for layout feel

If using color, muted tones with contrast (black/white, sepia, desaturated blues or greys) work well

Title: A Quiet Cartographer
Subtitle (optional placement): Not every narcissist is a monster. Some are just wounded men trying their best to survive
Author: Marlon Weskett

Deliverables:

Full front cover for print sale size as previous cover, including space for subtitle and author name

Spine and back cover (leave placeholder text if no blurb is given)

Ebook cover version

High-resolution files suitable for Quillmark QPS and print use

Additional Notes:
Please ensure the tone stays emotionally resonant, masculine, and sophisticated. No stock image models or cliché therapist symbols. Use my uploaded photos only.

Looking forward to seeing your vision come to life.

Back Cover Blurb – A Quiet Cartographer
A brutally honest recovery story—about what happens after you get clean, and the ego you still have to face.
Most people think addiction ends when you put down the drink, the drug, or the chaos.
But for Marlon Weskett, sobriety was just the start.
Behind the personal development posts, six-pack selfies, and billion-rand property deals, he was still chasing the one thing rehab never took from him: the need to be admired.
This book is not a confession. It’s a dismantling.
In A Quiet Cartographer, Marlon exposes the hidden patterns of ego, control, and validation-seeking that nearly cost him everything—even after he got “better.” With fearless self-inquiry and raw storytelling, he invites readers into his recovery from performance, perfectionism, and power addiction.
Whether you’ve been the narcissist—or you’ve loved one—this book is a mirror. And what you’ll find is not just insight, but a new path forward: one where truth is more powerful than charm, and safety matters more than being impressive.
This isn’t about being perfect.
It’s about being honest.
And finally becoming someone worth trusting—especially by yourself.

Target Market(s)

Any reader wanting to read about narcissism and love

Font styles to use
Sans Serif

Colors
EB3D1F
EC4F4E
F09395
F8D3D4
FCEDEE

Requirements
Must have
• Must be better than the mock design I uploaded.

```html
<!DOCTYPE html>
<html lang="en">
<head>
<meta charset="utf-8">
<title>A Quiet Cartographer — Cover Wrap</title>
<link rel="stylesheet" href="https://fonts.googleapis.com/css2?family=Anton&family=Oswald:wght@300;600&family=Roboto+Condensed:wght@300&family=Roboto:wght@400;700&display=swap">
<style>
  :root {
    --blush: #fcedee;
    --rose-light: #f8d3d4;
    --rose: #f09395;
    --coral: #ec4f4e;
    --signal-red: #eb3d1f;
    --night: #121a20;
    --slate: #2f4a5a;
    --slate-deep: #1c2c36;
    --mist: #dfe8ec;
    --body-ink: #1b1f22;
    --white: #ffffff;
  }
  * { margin: 0; padding: 0; box-sizing: border-box; }
  html, body { width: 1200px; height: 890px; overflow: hidden; background: var(--blush); }

  .cover-wrap { position: relative; width: 1200px; height: 890px; overflow: hidden; }

  /* Back cover */
  .back-cover {
    position: absolute; left: 0; top: 0; width: 575px; height: 890px;
    background: var(--blush);
  }
  .back-rule {
    position: absolute; left: 55px; top: 150px; width: 60px; height: 3px;
    background: var(--signal-red);
  }
  .blurb {
    position: absolute; left: 55px; top: 178px; width: 462px;
    font-family: "Roboto Condensed", sans-serif; font-weight: 300;
    font-size: 16.4px; line-height: 23.7px; color: var(--body-ink);
  }
  .blurb p.indent { text-indent: 13px; }

  /* Spine */
  .spine {
    position: absolute; left: 575px; top: 0; width: 50px; height: 890px;
    background: var(--night);
  }
  .spine-seam {
    position: absolute; left: 24px; top: 0; width: 2px; height: 40px;
    background: var(--signal-red);
  }
  .spine-title, .spine-author {
    position: absolute; left: 50%; white-space: nowrap;
    transform-origin: 0 0;
    font-family: "Oswald", sans-serif; font-size: 24px; line-height: 1;
    text-transform: uppercase; color: var(--white);
  }
  .spine-title { top: 70px; transform: rotate(90deg) translateY(-50%); }
  .spine-title .strong { font-weight: 600; }
  .spine-title .light { font-weight: 300; color: var(--coral); }
  .spine-author { top: 660px; font-weight: 300; letter-spacing: 2px; color: var(--rose-light); transform: rotate(90deg) translateY(-50%); }

  /* Front cover */
  .front-cover {
    position: absolute; left: 625px; top: 0; width: 575px; height: 890px;
    background: var(--night); overflow: hidden;
  }
  .author-name {
    position: absolute; left: 0; right: 0; top: 22px; text-align: center;
    font-family: "Oswald", sans-serif; font-weight: 300; font-size: 30px; line-height: 1;
    letter-spacing: 10px; text-indent: 10px; color: var(--white);
  }
  .portrait-split {
    position: absolute; left: 0; top: 78px; width: 575px; height: 522px;
  }
  .portrait-half { position: absolute; top: 0; height: 100%; width: 50%; }
  .portrait-clean {
    left: 0;
    background:
      radial-gradient(ellipse 90% 62% at 100% 44%, rgba(240,147,149,0.75) 0%, rgba(240,147,149,0) 70%),
      linear-gradient(180deg, var(--rose-light) 0%, #d9b3b3 70%, var(--night) 100%);
  }
  .portrait-raw {
    left: 50%;
    background:
      radial-gradient(ellipse 90% 62% at 0% 44%, rgba(47,74,90,0.9) 0%, rgba(47,74,90,0) 70%),
      linear-gradient(180deg, #3d5666 0%, var(--slate-deep) 70%, var(--night) 100%);
  }
  .fault-line {
    position: absolute; left: 286px; top: 0; width: 3px; height: 890px;
    background: var(--signal-red);
  }
  .title-block { position: absolute; left: 0; top: 0; width: 575px; height: 890px; }
  .title-kicker { font-family: "Oswald", sans-serif; font-weight: 300; letter-spacing: 14px; }
  .title-main { font-family: "Anton", sans-serif; }
  .warm-half { fill: var(--rose); }
  .cool-half { fill: var(--mist); }
  .tagline {
    position: absolute; left: 62px; top: 792px; width: 451px; text-align: center;
    font-family: "Roboto", sans-serif; font-weight: 400;
    font-size: 15px; line-height: 20px; color: var(--mist);
  }
  .tagline .key { font-weight: 700; color: var(--coral); }
</style>
</head>
<body>
<div class="cover-wrap">

  <section class="back-cover">
    <div class="back-rule"></div>
    <div class="blurb">
      <p class="indent">A brutally honest recovery story—about what happens after you get clean, and the ego you still have to face.</p>
      <p>Most people think addiction ends when you put down the drink, the drug, or the chaos.</p>
      <p>But for Marlon Weskett, sobriety was just the start.</p>
      <p class="indent">Behind the personal development posts, six-pack selfies, and billion-rand property deals, he was still chasing the one thing rehab never took from him: the need to be admired.</p>
      <p>This book is not a confession. It’s a dismantling.</p>
      <p class="indent">In A Quiet Cartographer, Marlon exposes the hidden patterns of ego, control, and validation-seeking that nearly cost him everything—even after he got “better.” With fearless self-inquiry and raw storytelling, he invites readers into his recovery from performance, perfectionism, and power addiction.</p>
      <p class="indent">Whether you’ve been the narcissist—or you’ve loved one—this book is a mirror. And what you’ll find is not just insight, but a new path forward: one where truth is more powerful than charm, and safety matters more than being impressive.</p>
      <p>This isn’t about being perfect.</p>
      <p>It’s about being honest.</p>
      <p class="indent">And finally becoming someone worth trusting—especially by yourself.</p>
    </div>
  </section>

  <section class="spine">
    <div class="spine-seam"></div>
    <div class="spine-title"><span class="strong">A </span><span class="light">Quiet </span><span class="strong">Cartographer</span></div>
    <div class="spine-author">Marlon Weskett</div>
  </section>

  <section class="front-cover">
    <div class="author-name">MARLON WESKETT</div>
    <div class="portrait-split" role="img" aria-label="The author's two portraits joined down the centre: on the left the clean, centred, lighter self in warm rose tones; on the right the raw, unkept, heavier self in desaturated slate blue">
      <div class="portrait-half portrait-clean"></div>
      <div class="portrait-half portrait-raw"></div>
    </div>
    <div class="fault-line"></div>
    <svg class="title-block" viewBox="0 0 575 890" aria-label="A Quiet Cartographer">
      <defs>
        <clipPath id="left-side"><rect x="0" y="0" width="286" height="890"/></clipPath>
        <clipPath id="right-side"><rect x="289" y="0" width="286" height="890"/></clipPath>
      </defs>
      <g clip-path="url(#left-side)" class="warm-half">
        <text class="title-kicker" x="294.5" y="666" font-size="34" text-anchor="middle">A QUIET</text>
        <text class="title-main" x="287.5" y="766" font-size="92" text-anchor="middle" textLength="505" lengthAdjust="spacingAndGlyphs">CARTOGRAPHER</text>
      </g>
      <g clip-path="url(#right-side)" class="cool-half">
        <text class="title-kicker" x="294.5" y="666" font-size="34" text-anchor="middle">A QUIET</text>
        <text class="title-main" x="287.5" y="766" font-size="92" text-anchor="middle" textLength="505" lengthAdjust="spacingAndGlyphs">CARTOGRAPHER</text>
      </g>
    </svg>
    <p class="tagline">Not every <span class="key">narcissist</span> is a monster.<br>Some are just wounded men trying their best to survive.</p>
  </section>

</div>
</body>
</html>
```